Flyer-Design für bildenden Künstler
Die einzige Designerin, die es wirklich verstanden hat, mein ausführliches briefing in einem wunderschönen, eleganten und absolut einzigartigen Design umzusetzen. Die Zusammenarbeit war klasse, sie ist auf jede meiner Wünsche eingegangen und hat sie mit großer Geduld und Professionalität umgesetzt. Das hätte nicht besser laufen können. Bin begeistert, von ihrem künstlerischen Anspruch, dem feinen Sinn für Ästhetik und ihrer großen Kreativität.
Zielgruppe
Ich bin bildender Künstler, benötige einen außergewöhnlichen, sehr ästhetischen, einzigartigen, als Eyecatcher fungierenden, meine Kunst und Identität repräsentierenden Flyer zum Auslegen, um neue KundInnen zu gewinnen.
Aufgabenstellung
Er soll wenig Text beinhalten (ein Zitat, Anschrift und Kontaktmöglichkeiten, ein kleines statement zu meiner Kunstphilosophie), und Bilder meiner Kunst zeigen. Raum ist mir wichtig, genug Leerräume, damit ein in Szene gesetztes Zitat oder Foto meiner Kunstwerke gut wirken kann. Es soll Lust darauf machen, Anreiz bieten und Interesse wecken, auf meine homepage zu gehen. Die Einzigartigkeit meiner Kunst soll deutlich werden.
Die hochgelandenen Fotos zeigen meine Kunstwerke. Sie können als Hintergrundbild fungieren und dementsprechend auch die ganze Seite ausfüllen, sie können zugeschnitten werden und/oder mit Text überlagert sein. Manche Fotos (zum Beispiel die Kunstwerke mit Rahmen) eignen sich dagegen, sie auf einer ganzen Seite zu zeigen, ohne einen Text dazu. So eine Seite würde ich jedenfalls gerne dabei haben, wo ein Kunstwerk für sich alleine auf einer ganzen Seite dargestellt wird. 1O4A2598 oder 1O4A6076a bieten sich dafür an (diese und alle anderen Fotos sind zum Teil komprimiert und zugeschnitten; falls gewünscht bzw. die Qualität nicht gut ist, kann ich das Originalfoto senden, das unkomprimiert und nicht zugeschnitten ist. Auch kann die Helligkeit oder die Farbqualität verbessert werden, falls notwendig). Nicht alle Kunstbilder müssen verwendet werden.
Ich bin offen für jedes Flyerformat, tendiere zu einem ein 2 oder 3-seitigen Falzflyer hochkant oder im Querformat. Bin aber offen für Ideen und Vorschläge.
Die Texte unter der Datei 'Texte, Adresse, Zitate' enthalten einen kleinen Text, der verwendet werden soll. Unter 'Text für die Titelseite' ist ein Vorschlag für die Titelseite zu finden. Die Adresse muss vollständig erscheinen, und unter 'Zitate' sind mehrere meiner Zitate - auch davon soll eines verwendet werden.
BITTE AUSSCHLIEßLICH DIE FOTOS UND TEXTE VERWENDEN, DIE ICH HOCHGELADEN HABE, UND NICHTS VON MEINEN HOMEPAGES NEHMEN. DANKE!

```html
<!DOCTYPE html>
<html lang="de">
<head>
<meta charset="utf-8">
<title>Atelier Wendt – Falzflyer</title>
<link href="https://fonts.googleapis.com/css2?family=Montserrat:wght@400;500;700;800&display=swap" rel="stylesheet">
<style>
  :root {
    --backdrop: #7f98aa;
    --steel-blue: #6e8ea3;
    --steel-dark: #4c6577;
    --paper: #f6f6f6;
    --title-teal: #2d6781;
    --ink-blue: #577c93;
    --ink-dark: #3a3f44;
    --art-teal: #3a9cc0;
    --art-deep: #1f6784;
    --frame-grey: #9a9a9a;
    --white: #ffffff;
  }
  * { box-sizing: border-box; margin: 0; padding: 0; }
  html, body { width: 1200px; height: 900px; overflow: hidden; }
  body {
    background: var(--backdrop);
    font-family: "Montserrat", sans-serif;
    display: flex;
    align-items: center;
    justify-content: center;
    gap: 40px;
  }
  .spread {
    width: 560px;
    height: 400px;
    display: grid;
    grid-template-columns: repeat(3, 1fr);
    box-shadow: 0 14px 30px rgba(30, 45, 58, 0.35);
  }
  .panel { position: relative; overflow: hidden; }

  /* outside: quote panel */
  .panel--quote {
    background: var(--steel-blue);
    color: var(--white);
    display: flex;
    flex-direction: column;
    align-items: center;
    justify-content: center;
    padding: 0 14px 50px;
    text-align: center;
  }
  .quote-mark { width: 26px; height: 18px; margin-bottom: 22px; }
  .quote-text { font-weight: 700; font-size: 10.5px; line-height: 1.7; max-width: 150px; }

  /* outside: contact panel */
  .panel--contact { background: var(--paper); }
  .contact {
    position: absolute;
    left: 0; right: 0; bottom: 62px;
    text-align: center;
    color: var(--ink-blue);
    font-style: normal;
    font-size: 8px;
    line-height: 1.3;
  }
  .contact__name { font-weight: 700; }
  .contact__gap { height: 10px; }
  .band {
    position: absolute;
    left: 0; right: 0; bottom: 0;
    height: 40px;
    background: var(--steel-blue);
  }
  .band--dark { background: var(--steel-dark); }
  .website {
    display: flex; align-items: center; justify-content: center;
    color: var(--white); font-weight: 700; font-size: 8px;
  }

  /* cover */
  .panel--cover { background: linear-gradient(90deg, #e2e2e2, #cfcfcf); }
  .brand {
    position: absolute;
    top: 28px; right: 14px;
    font-weight: 500;
    font-size: 13px;
    letter-spacing: 0.02em;
    color: var(--ink-dark);
  }
  .cover-rule {
    position: absolute;
    top: 56px; bottom: 0; right: 22px;
    width: 2px;
    background: var(--ink-blue);
  }
  .cover-title {
    position: absolute;
    left: 18px; bottom: 58px;
    writing-mode: vertical-rl;
    transform: rotate(180deg);
    font-weight: 800;
    font-size: 21px;
    line-height: 1.05;
    letter-spacing: 0.01em;
    color: var(--title-teal);
    text-transform: uppercase;
  }
  .cover-title__gap { display: inline-block; width: 6px; }

  /* inside */
  .panel--art-grey { background: linear-gradient(90deg, #ececec, #cdcdcd); }
  .panel--art-white { background: var(--paper); }
  .artwork-frame {
    position: absolute;
    top: 30px; bottom: 30px; left: 18px; right: 18px;
    border: 3px solid var(--frame-grey);
    background: #4a4a4a;
    padding: 3px;
  }
  .artwork {
    width: 100%; height: 100%;
    background: radial-gradient(circle at 40% 35%, var(--art-teal), var(--art-deep));
  }
  .panel--philosophy {
    background: linear-gradient(90deg, #f6f6f6, #e4e4e4);
    color: var(--ink-blue);
    padding: 50px 14px 0 22px;
  }
  .philosophy__title { font-weight: 800; font-size: 18px; line-height: 1.3; }
  .philosophy__rule { width: 18px; height: 2px; background: var(--ink-blue); margin: 14px 0 24px; }
  .philosophy__text { font-size: 9px; line-height: 1.45; }
  .panel--philosophy .brand { top: auto; bottom: 22px; }
</style>
</head>
<body>

  <section class="spread spread--outside" aria-label="Außenseite">
    <div class="panel panel--quote">
      <svg class="quote-mark" viewBox="0 0 28 20" aria-hidden="true">
        <path fill="#ffffff" d="M6 20a6 6 0 0 1-6-6c0-6 4-12 10-14l1 2c-3 2-5 4-5 6a6 6 0 0 1 0 12zm15 0a6 6 0 0 1-6-6c0-6 4-12 10-14l1 2c-3 2-5 4-5 6a6 6 0 0 1 0 12z"/>
      </svg>
      <p class="quote-text">Kunst unterstreicht Deinen guten Geschmack. Es zeugt davon, dass Du Weitblick besitzt. Und offen für neue Erfahrungen bist.</p>
    </div>

    <div class="panel panel--contact">
      <address class="contact">
        <div class="contact__name">Tobias Wendt</div>
        <div>Lindenhof-Str. 12</div>
        <div>79100 Lindenau</div>
        <div class="contact__gap"></div>
        <div>(+49) 0761 555 0172</div>
        <div>atelier@wendt-studio.example</div>
      </address>
      <div class="band website">www.wendt-studio.example</div>
    </div>

    <div class="panel panel--cover">
      <div class="brand">Atelier Wendt</div>
      <h1 class="cover-title">Tobias<br>Wendt Atelier<br><span class="cover-title__gap"></span>Transfor<br>mationen</h1>
      <div class="band band--dark"></div>
      <div class="cover-rule"></div>
    </div>
  </section>

  <section class="spread spread--inside" aria-label="Innenseite">
    <div class="panel panel--art-grey">
      <div class="artwork-frame">
        <div class="artwork" role="img" aria-label="Gerahmtes Kunstwerk aus blau eingefärbtem Moos"></div>
      </div>
    </div>

    <div class="panel panel--philosophy">
      <h2 class="philosophy__title">The<br>Philosophy</h2>
      <div class="philosophy__rule"></div>
      <p class="philosophy__text">Seit jeher fasziniert mich die Transformation eines Zustandes in einen anderen. Das ganze Leben ist eine fortwährende Veränderung, nichts bleibt, wie es ist. Ich setze mich damit auseinander und gebe Material und Vergangenem eine neue Sinnhaftigkeit.</p>
      <div class="brand">Atelier Wendt</div>
    </div>

    <div class="panel panel--art-white">
      <div class="artwork-frame">
        <div class="artwork" role="img" aria-label="Gerahmtes Kunstwerk aus türkisblauem Moos"></div>
      </div>
    </div>
  </section>

</body>
</html>
```